Visitenkarten-Design für Pflegedienst
Zielgruppe
Pflegedienst
Aufgabenstellung
Siehe Beispielvisitenkarte. Es soll so ähnlich designt werden mit hochwertigem Papier. Die Angaben darauf sind auch schon korrekt.

```html
<!DOCTYPE html>
<html lang="de">
<head>
<meta charset="utf-8">
<title>Visitenkarte Luftpflege24</title>
<link href="https://fonts.googleapis.com/css2?family=Roboto:wght@400;500&display=swap" rel="stylesheet">
<style>
  :root {
    --blue-dark: #22427f;
    --blue-mid: #4a70b8;
    --blue-text: #2f4a8a;
    --ink: #1a1a1a;
    --paper: #ffffff;
    --bg: #f4f4f4;
  }
  * { box-sizing: border-box; margin: 0; padding: 0; }
  html, body { width: 1200px; height: 1200px; overflow: hidden; }
  body {
    background: var(--bg);
    font-family: "Roboto", Arial, sans-serif;
    color: var(--ink);
    position: relative;
  }
  .card {
    position: absolute;
    left: 220px;
    width: 760px;
    height: 436px;
    background: var(--paper);
    box-shadow: 6px 8px 10px rgba(0,0,0,0.35);
    overflow: hidden;
  }
  .card--front { top: 140px; }
  .card--back { top: 626px; }
  .band {
    position: absolute;
    left: 0; right: 0;
    background: linear-gradient(90deg, var(--blue-dark) 0%, var(--blue-mid) 22%, var(--blue-mid) 78%, var(--blue-dark) 100%);
    color: #fff;
    display: flex; align-items: center; justify-content: center;
  }
  .band--name { top: 38px; height: 66px; font-size: 45px; letter-spacing: 0.5px; }
  .role {
    position: absolute; top: 114px; left: 0; right: 0;
    text-align: center; font-size: 22px;
  }
  .contact { position: absolute; left: 40px; font-size: 18.5px; line-height: 24px; }
  .contact__address { top: 212px; display: flex; gap: 8px; }
  .contact__address .icon { margin-top: 2px; }
  .contact__company { font-weight: 500; }
  .contact__phones { top: 272px; left: 44px; }
  .contact__mail { top: 356px; display: flex; align-items: center; gap: 12px; }
  .divider-v {
    position: absolute; left: 415px; top: 199px; width: 2px; height: 197px;
    background: #222;
  }
  .portrait {
    position: absolute; left: 496px; top: 162px; width: 180px; height: 244px;
    background: linear-gradient(180deg, #ececec 0%, #d9d6d2 45%, #f6f6f6 100%);
  }
  .brand {
    position: absolute; left: 0; right: 0; top: 0; bottom: 60px;
    display: flex; align-items: center; justify-content: center; gap: 22px;
  }
  .brand__dot {
    width: 56px; height: 56px; border-radius: 50%; background: var(--blue-text);
  }
  .brand__name {
    font-size: 42px; font-weight: 400; color: var(--blue-text);
  }
  .band--web { bottom: 0; height: 60px; font-size: 31px; }
</style>
</head>
<body>
  <section class="card card--front">
    <div class="band band--name">MAREK BRANDOVIĆ LL.M.</div>
    <p class="role">Wirtschaftsjurist | Geschäftsführer</p>

    <div class="contact contact__address">
      <svg class="icon" width="16" height="20" viewBox="0 0 16 20"><path d="M8 1a6.5 6.5 0 0 0-6.5 6.5C1.5 12 8 19 8 19s6.5-7 6.5-11.5A6.5 6.5 0 0 0 8 1z" fill="none" stroke="#111" stroke-width="1.8"/><circle cx="8" cy="7.5" r="2.3" fill="none" stroke="#111" stroke-width="1.8"/></svg>
      <div>
        <div class="contact__company">Luftpflege24 GmbH,</div>
        <div>Wiesentaler Str. 12. 71234 Musterfeld</div>
      </div>
    </div>

    <div class="contact contact__phones">
      <div>M +49 151 40302010</div>
      <div>T &nbsp;+49 7000 1234500</div>
      <div>F &nbsp;+49 7000 1234502</div>
    </div>

    <div class="contact contact__mail">
      <svg width="18" height="13" viewBox="0 0 18 13"><rect x="1" y="1" width="16" height="11" fill="none" stroke="#111" stroke-width="1.6"/><path d="M1 1l8 6 8-6M1 12l6-5M17 12l-6-5" fill="none" stroke="#111" stroke-width="1.4"/></svg>
      <span>mb@luftpflege24.de</span>
    </div>

    <div class="divider-v"></div>
    <div class="portrait" role="img" aria-label="Porträtfoto des Geschäftsführers im weißen Hemd"></div>
  </section>

  <section class="card card--back">
    <div class="brand">
      <div class="brand__dot"></div>
      <div class="brand__name">Luftpflege24 GmbH</div>
    </div>
    <div class="band band--web">www.luftpflege24.de</div>
  </section>
</body>
</html>
```